Shopify Web-Page "Tovi-BrambleDays

We are building a new business in Switzerland offering premium sewing holiday camps for kids aged 9–14. In enclosed brief outlines our requirements for a complete Shopify homepage design and a multilingual logo creation.
Domains: tovi-brambledays.ch ; tovi-giornirovo.ch ; tovi-brombeertage.ch

Project Overview
We are looking for:
1. A modern, fully designed Shopify homepage in English using standard Shopify content blocks (no custom coding), which we can later update ourselves. Supporting Multilanguage (EN, German, Italian).

2. A logo design that includes the brand identity and communicates our multilingual, creative, and child-focused positioning.

All details in enclosed

```html
<!DOCTYPE html>
<html lang="en">
<head>
<meta charset="utf-8">
<title>Tovi-BrambleDays – Sewing Holiday Camps for Kids</title>
<link rel="stylesheet" href="https://fonts.googleapis.com/css2?family=Lilita+One&family=Poppins:wght@400;500;600;700&display=swap">
<style>
:root{
  --pink:#e8547a;
  --yellow:#f2bd1d;
  --blue:#2aa3d8;
  --teal:#5fd0b2;
  --green:#8bcf6a;
  --navy:#16243a;
  --ink:#1f2a37;
  --muted:#5d6673;
  --sky:#e7f3fa;
  --band:#38ace0;
  --line:#e6e9ee;
}
*{box-sizing:border-box;margin:0;padding:0}
html,body{width:1200px;height:4906px;overflow:hidden}
body{position:relative;background:#fff;font-family:"Poppins",sans-serif;color:var(--ink)}
.abs{position:absolute}
.label{position:absolute;left:0;width:1200px;text-align:center;font-size:14px;font-weight:600;color:var(--blue);letter-spacing:.3px}
.heading{position:absolute;left:0;width:1200px;text-align:center;font-size:25px;font-weight:500;letter-spacing:.4px;text-transform:uppercase}
.heading em,.about-title em{font-style:normal;color:var(--pink);font-weight:600;text-decoration:underline;text-decoration-thickness:2px;text-underline-offset:6px}

/* header */
.site-header{position:absolute;top:0;left:0;width:1200px;height:78px;background:#fff;z-index:3}
.logo-box{position:absolute;left:99px;top:0;width:198px;height:168px;background:#fff;border-radius:0 0 18px 18px;box-shadow:0 6px 20px rgba(0,0,0,.08);display:flex;align-items:center;justify-content:center;z-index:4}
.brand{font-family:"Poppins",sans-serif;font-weight:700;color:var(--pink);font-size:19px}
.nav{position:absolute;top:29px;left:368px;display:flex;gap:0;font-size:13px}
.nav a{position:absolute;white-space:nowrap;color:var(--ink);text-decoration:none}
.lang{position:absolute;left:825px;top:29px;font-size:13px;display:flex;align-items:center;gap:6px}
.btn{display:flex;align-items:center;justify-content:center;gap:10px;border-radius:22px;font-size:13px;color:#fff;font-weight:500}
.btn .dot{width:22px;height:22px;border-radius:50%;background:#fff;display:flex;align-items:center;justify-content:center}
.contact-btn{position:absolute;left:935px;top:21px;width:122px;height:36px;background:var(--pink)}

/* hero */
.hero-photo{position:absolute;top:78px;left:0;width:1200px;height:560px;background:linear-gradient(90deg,#f6f5f3 0%,#f1eeea 38%,#d9cfc4 60%,#b9a999 80%,#8f7f73 100%)}
.hero-wave{position:absolute;top:540px;left:0}
.hero-title{position:absolute;left:99px;top:204px;font-family:"Lilita One",sans-serif;font-size:42px;line-height:49px;letter-spacing:1px}
.hero-title .l1{color:var(--pink)}.hero-title .l2{color:var(--yellow)}.hero-title .l3{color:var(--blue)}
.hero-text{position:absolute;left:99px;top:356px;width:380px;font-size:13.5px;line-height:23px}
.hero-btn{position:absolute;left:99px;top:463px;width:204px;height:40px;background:var(--blue)}
.hero-join{position:absolute;left:99px;top:535px;font-size:13.5px;display:flex;gap:10px;align-items:center}

/* about */
.about-art{position:absolute;left:141px;top:705px;width:421px;height:421px}
.about-label{position:absolute;left:600px;top:707px;font-size:14px;font-weight:600;color:var(--blue)}
.about-title{position:absolute;left:600px;top:738px;font-size:25px;font-weight:500}
.about-text{position:absolute;left:600px;top:793px;width:460px;font-size:12.5px;line-height:20.5px;color:var(--ink)}
.about-text p{margin-bottom:18px}
.person{position:absolute;top:1012px;display:flex;gap:16px;align-items:center}
.person .ph{width:68px;height:68px;border-radius:50%;background:linear-gradient(135deg,#d8c8bd,#6f5a4e)}
.person b{display:block;font-size:16px;font-weight:600}
.person span{font-size:13px;color:var(--muted)}

/* how it works */
.how-bg{position:absolute;top:1195px;left:0}
.step{position:absolute;top:1419px;width:170px;height:210px;background:#fff;border-radius:6px;box-shadow:0 4px 14px rgba(30,60,90,.06);padding:0 14px}
.step .ic{position:absolute;left:14px;top:-18px;width:76px;height:80px;border-radius:50% 50% 50% 50%/55% 55% 45% 45%;display:flex;align-items:center;justify-content:center}
.step .ic i{width:54px;height:54px;border-radius:50%;border:2px solid rgba(255,255,255,.7);display:flex;align-items:center;justify-content:center}
.step .num{position:absolute;right:14px;top:10px;font-size:40px;font-weight:700;color:#eef0f3}
.step h4{position:absolute;top:82px;left:14px;font-size:14px;font-weight:500}
.step p{position:absolute;top:106px;left:14px;width:144px;font-size:11.5px;line-height:19.5px;color:var(--muted)}

/* why */
.why-ring{position:absolute;left:450px;top:1955px;width:300px;height:300px;border:2px dashed #888;border-radius:50%}
.why-core{position:absolute;left:476px;top:1981px;width:248px;height:248px;border-radius:50%;background:#fff;box-shadow:0 6px 30px rgba(0,0,0,.12);display:flex;align-items:center;justify-content:center}
.why-ic{position:absolute;width:70px;height:70px;border-radius:50%;display:flex;align-items:center;justify-content:center}
.why-t{position:absolute;font-size:13.5px;line-height:24px}
.why-t.r{text-align:right}
.divider{position:absolute;left:141px;top:2346px;width:918px;height:1px;background:var(--line)}

/* camps */
.camp{position:absolute;top:2511px;width:282px;height:372px;border:1px solid var(--line);border-radius:6px;overflow:hidden;background:#fff}
.camp .img{height:162px;background:linear-gradient(135deg,#c9b3a2,#8e7a6d 60%,#e6ddd4)}
.camp h4{font-size:14px;font-weight:500;margin:14px 15px 4px}
.camp p{font-size:11.5px;line-height:20px;color:var(--muted);margin:0 15px;height:84px}
.camp .meta{display:grid;grid-template-columns:42px 95px 52px 1fr;margin:6px 15px 0;font-size:11.5px;row-gap:11px}
.camp .meta b{font-weight:600}
.camp .meta span{color:var(--muted)}
.all-btn{position:absolute;left:518px;top:2915px;width:164px;height:38px;background:var(--pink);box-shadow:0 0 0 3px #f7c9d5}

/* cta */
.cta-bg{position:absolute;top:3050px;left:0}
.cta-title{position:absolute;top:3150px;left:0;width:1200px;text-align:center;font-family:"Lilita One",sans-serif;font-size:37px;color:#fff;letter-spacing:1.5px}
.cta-text{position:absolute;top:3212px;left:290px;width:620px;text-align:center;color:#fff;font-size:14px;line-height:25px}
.cta-btn{position:absolute;left:518px;top:3298px;width:164px;height:38px;background:#fff;color:var(--blue);box-shadow:0 0 0 3px rgba(255,255,255,.4)}
.cta-btn .dot{background:var(--blue)}

/* faq */
.faq{position:absolute;left:177px;width:846px;height:66px;background:#fff;box-shadow:0 4px 14px rgba(20,40,70,.07);border-left:2px solid var(--pink);display:flex;align-items:center;padding:0 24px;font-size:14px;font-weight:500}
.faq svg{position:absolute;right:22px;top:26px}
.faq.open{height:112px;border:1px solid var(--pink);border-left-width:2px;display:block;padding:22px 24px}
.faq.open p{font-size:11.5px;font-weight:400;line-height:21px;color:var(--muted);margin-top:12px;width:720px}
.to-top{position:absolute;left:1098px;top:4483px;width:40px;height:40px;border-radius:50%;background:var(--pink);display:flex;align-items:center;justify-content:center}

/* footer */
.footer-bg{position:absolute;top:4548px;left:0}
.footer-brand{position:absolute;left:143px;top:4670px;color:var(--pink);font-weight:700;font-size:20px}
.f-head{position:absolute;top:4642px;color:var(--yellow);font-size:15px;font-weight:500}
.f-links{position:absolute;left:364px;top:4682px;font-size:12px;color:#fff;line-height:29px}
.f-contact{position:absolute;left:516px;font-size:12px;color:#fff;line-height:21px;display:flex;gap:16px;align-items:center}
.f-contact i{width:32px;height:32px;border-radius:50%;display:flex;align-items:center;justify-content:center;flex:none}
.f-sub{position:absolute;left:812px;top:4680px;width:250px;color:#fff;font-size:12px;line-height:22px}
.f-input{position:absolute;left:812px;top:4768px;width:246px;height:32px;background:#fff;border-radius:18px;font-size:11px;color:#9aa;display:flex;align-items:center;padding-left:14px}
.f-input i{position:absolute;right:4px;top:3px;width:26px;height:26px;border-radius:50%;background:var(--blue);display:flex;align-items:center;justify-content:center}
.follow{position:absolute;left:143px;top:4792px;color:#fff;font-size:12px;display:flex;gap:8px;align-items:center}
.follow i{width:20px;height:20px;border-radius:50%;border:1px solid #fff;display:block}
.copyright{position:absolute;left:0;top:4872px;width:1200px;text-align:center;color:#fff;font-size:11px}
.f-rule{position:absolute;left:0;top:4858px;width:1200px;height:1px;background:rgba(255,255,255,.12)}
</style>
</head>
<body>

<!-- Header -->
<header class="site-header">
  <nav class="nav">
    <a style="left:0;font-weight:600">Home</a>
    <a style="left:59px">About Us</a>
    <a style="left:141px">Camps</a>
    <a style="left:207px">How It Works</a>
    <a style="left:312px">FAQs</a>
    <a style="left:367px">Contact</a>
  </nav>
  <div class="lang">
    <svg width="14" height="14" viewBox="0 0 14 14"><circle cx="7" cy="7" r="6" fill="none" stroke="#1f2a37"/><ellipse cx="7" cy="7" rx="2.6" ry="6" fill="none" stroke="#1f2a37"/><path d="M1 7h12" stroke="#1f2a37"/></svg>
    English
    <svg width="12" height="8" viewBox="0 0 12 8" style="margin-left:14px"><path d="M1 1l5 5 5-5" fill="none" stroke="#1f2a37" stroke-width="1.6"/></svg>
  </div>
  <div class="btn contact-btn">Contact Us <span class="dot"><svg width="10" height="10" viewBox="0 0 10 10"><path d="M2 8L8 2M3 2h5v5" fill="none" stroke="#e8547a" stroke-width="1.6"/></svg></span></div>
</header>
<div class="logo-box"><span class="brand">Tovi-BrambleDays</span></div>

<!-- Hero -->
<section>
  <div class="hero-photo" role="img" aria-label="Photo of girls working at a sewing machine with an instructor in a bright workshop"></div>
  <svg class="hero-wave" width="1200" height="100" viewBox="0 0 1200 100"><path d="M0 40 C200 100 420 100 640 60 C860 20 1040 10 1200 50 L1200 100 L0 100Z" fill="#fff"/></svg>
  <h1 class="hero-title"><span class="l1">PREMIUM SEWING</span><br><span class="l2">HOLIDAY CAMPS FOR</span><br><span class="l3">KIDS 9-14</span></h1>
  <p class="hero-text">Creative fun in Zurich – Multilingual and Inspiring! Learn sewing, build confidence, and create unique fashion pieces in our small-group camps.</p>
  <div class="btn hero-btn">View Upcoming Camps <span class="dot"><svg width="10" height="10" viewBox="0 0 10 10"><path d="M2 8L8 2M3 2h5v5" fill="none" stroke="#2aa3d8" stroke-width="1.6"/></svg></span></div>
  <div class="hero-join"><svg width="20" height="20" viewBox="0 0 20 20"><circle cx="10" cy="10" r="8.5" fill="none" stroke="#1f2a37" stroke-width="1.4"/><circle cx="7" cy="8" r="1" fill="#1f2a37"/><circle cx="13" cy="8" r="1" fill="#1f2a37"/><path d="M6 12c2 2.5 6 2.5 8 0" fill="none" stroke="#1f2a37" stroke-width="1.4"/></svg>Join 200+ happy campers!</div>
</section>

<!-- About -->
<section>
  <svg class="about-art" viewBox="0 0 421 421">
    <g role="img" aria-label="Photo collage of children sewing, set in a circle">
      <path d="M206 206 L206 0 A206 206 0 0 0 0 206Z" fill="#b9a295"/>
      <path d="M206 206 L0 206 A206 206 0 0 0 206 412Z" fill="#d9cdc6"/>
      <path d="M214 214 L420 214 A206 206 0 0 1 214 420Z" fill="#c9a79d"/>
    </g>
    <path d="M214 198 L214 0 A206 206 0 0 1 420 198Z" fill="#f2bd1d"/>
    <path d="M214 198 L214 40 A158 158 0 0 1 372 198Z" fill="#e8709a"/>
    <circle cx="210" cy="202" r="30" fill="#fff"/>
    <circle cx="210" cy="202" r="24" fill="#fff" stroke="#f2bd1d" stroke-width="3"/>
    <path d="M210 213 l-9-9a5.5 5.5 0 0 1 9-6a5.5 5.5 0 0 1 9 6z" fill="#2aa3d8"/>
  </svg>
  <div class="about-label">ABOUT OUR CAMPS</div>
  <h2 class="about-title">LEARNING WITH FUN <em>&amp; STRUCTURE</em></h2>
  <div class="about-text">
    <p>At Tovi-BrambleDays, we believe in nurturing creativity while having fun. Our experienced instructors create a safe, inspiring environment where children can explore their creative potential.</p>
    <p>With over 10 years of experience in teaching children sewing, tailoring, and design, Marlene and Nadia guide young talents through a creative week of vacation – with real results: self-sewn pieces, new friends, and lots of pride.</p>
    <p>At the last day, the children show off their success, their own sewn unique pieces, in a sympathetic fashion show.</p>
  </div>
  <div class="person" style="left:600px"><div class="ph" role="img" aria-label="Portrait of the sewing expert"></div><div><b>Marlene</b><span>Sewing Expert</span></div></div>
  <div class="person" style="left:818px"><div class="ph" role="img" aria-label="Portrait of the design specialist"></div><div><b>Nadia</b><span>Design Specialist</span></div></div>
</section>

<!-- How it works -->
<section>
  <svg class="how-bg" width="1200" height="545" viewBox="0 0 1200 545"><path d="M0 40 C250 -10 520 60 760 20 C960 -10 1100 10 1200 30 L1200 500 C1000 540 780 480 560 510 C340 540 160 500 0 520Z" fill="#e7f3fa"/></svg>
  <div class="label" style="top:1329px">HOW OUR CAMPS WORK</div>
  <h2 class="heading" style="top:1358px">Creative holiday camps for young <em>sewing champs!</em></h2>

  <div class="step" style="left:141px"><div class="ic" style="background:#ee6a7f"><i><svg width="26" height="22" viewBox="0 0 26 22"><circle cx="13" cy="6" r="4" fill="#fff"/><circle cx="5" cy="8" r="3" fill="#fff"/><circle cx="21" cy="8" r="3" fill="#fff"/><path d="M6 21c0-5 3-8 7-8s7 3 7 8zM0 20c0-4 2-6 5-6M26 20c0-4-2-6-5-6" fill="#fff"/></svg></i></div><span class="num">01</span><h4>Project Selection</h4><p>Your child chooses their own model based on previously produced clothing items and sewing patterns.</p></div>
  <div class="step" style="left:328px"><div class="ic" style="background:var(--teal)"><i><svg width="24" height="24" viewBox="0 0 24 24" fill="none" stroke="#fff" stroke-width="1.6"><rect x="2" y="2" width="20" height="20" rx="2"/><path d="M8 2v20M16 2v20M2 8h20M2 16h20"/></svg></i></div><span class="num">02</span><h4>Fabric selection</h4><p>High-quality fabrics are available.</p></div>
  <div class="step" style="left:515px"><div class="ic" style="background:#ea5a79"><i><svg width="26" height="22" viewBox="0 0 26 22" fill="#fff"><path d="M3 4h18a3 3 0 0 1 3 3v4H11v7H3z"/><rect x="2" y="18" width="22" height="3" rx="1"/></svg></i></div><span class="num">03</span><h4>Sewing machine</h4><p>Learn how to use a sewing machine</p></div>
  <div class="step" style="left:702px"><div class="ic" style="background:#f4c340"><i><svg width="24" height="24" viewBox="0 0 24 24" fill="none" stroke="#fff" stroke-width="2"><path d="M4 20l3-1 12-12-2-2L5 17zM15 5l4 4"/></svg></i></div><span class="num">04</span><h4>Sewing &amp; refining</h4><p>Step by step to the goal with professional guidance</p></div>
  <div class="step" style="left:889px"><div class="ic" style="background:var(--green)"><i><svg width="26" height="20" viewBox="0 0 26 20" fill="#fff"><rect x="1" y="6" width="17" height="13" rx="2"/><path d="M18 11l7-4v11l-7-4z"/><circle cx="6" cy="4" r="3"/><circle cx="13" cy="4" r="3"/></svg></i></div><span class="num">05</span><h4>Showtime!</h4><p>Fashion show or photo shoot at the end of the week</p></div>
</section>

<!-- Why families -->
<section>
  <div class="label" style="top:1838px">WHY PARENTS CHOOSE US</div>
  <h2 class="heading" style="top:1867px">Why families love Tovi-BrambleDays sewing <em>camps</em></h2>
  <div class="why-ring"></div>
  <div class="why-core"><span class="brand" style="font-size:20px">Tovi-BrambleDays</span></div>

  <div class="why-t r" style="left:130px;top:1957px;width:204px">Small groups &amp;<br>personalized attention</div>
  <div class="why-ic" style="left:343px;top:1946px;background:#f8d777"><svg width="28" height="28" viewBox="0 0 28 28" fill="none" stroke="#fff" stroke-width="2.2"><path d="M4 4l8 8M12 6v6H6M24 24l-8-8M16 22v-6h6"/></svg></div>
  <div class="why-t r" style="left:100px;top:2081px;width:204px">Multilingual supervision<br>(DE / EN / IT)</div>
  <div class="why-ic" style="left:319px;top:2070px;background:var(--teal)"><svg width="30" height="30" viewBox="0 0 30 30" fill="none" stroke="#fff" stroke-width="2"><path d="M3 6h14M10 3v3M6 6c1 5 5 9 9 11M14 6c-1 5-5 9-10 11M15 27l5-13 5 13M17 22h6"/></svg></div>
  <div class="why-t r" style="left:130px;top:2205px;width:204px">Pick-up Service from the<br>Main-Station</div>
  <div class="why-ic" style="left:343px;top:2194px;background:var(--pink)"><svg width="24" height="28" viewBox="0 0 24 28"><path d="M12 27s9-9 9-15a9 9 0 0 0-18 0c0 6 9 15 9 15z" fill="#fff"/><circle cx="12" cy="12" r="3.5" fill="#e8547a"/></svg></div>

  <div class="why-ic" style="left:773px;top:1946px;background:var(--teal)"><svg width="30" height="30" viewBox="0 0 30 30"><path d="M15 3l3.6 7.6 8.2 1-6 5.7 1.6 8.2L15 21.5l-7.4 4 1.6-8.2-6-5.7 8.2-1z" fill="none" stroke="#fff" stroke-width="2"/></svg></div>
  <div class="why-t" style="left:853px;top:1944px;width:210px">Encouragement of creativity, self-confidence, and fine motor skills</div>
  <div class="why-ic" style="left:799px;top:2070px;background:var(--pink)"><svg width="26" height="30" viewBox="0 0 26 30" fill="none" stroke="#fff" stroke-width="2"><path d="M13 2l10 4v8c0 7-5 11-10 14C8 25 3 21 3 14V6z"/><path d="M8 15l4 4 6-7"/></svg></div>
  <div class="why-t" style="left:879px;top:2069px;width:190px">Safe, loving environment in Zurich, various places easy to reach</div>
  <div class="why-ic" style="left:773px;top:2194px;background:#f8d777"><svg width="28" height="28" viewBox="0 0 28 28" fill="none" stroke="#fff" stroke-width="1.8"><rect x="3" y="3" width="22" height="22" rx="2"/><path d="M10 3v22M18 3v22M3 10h22M3 18h22"/></svg></div>
  <div class="why-t" style="left:853px;top:2193px;width:200px">High-quality fabrics &amp; top-quality sewing machines (Veltra)</div>
  <div class="divider"></div>
</section>

<!-- Upcoming camps -->
<section>
  <div class="label" style="top:2425px">OUR UPCOMING CAMPS</div>
  <h2 class="heading" style="top:2453px">Multilingual creativity, made just <em>for kids</em></h2>

  <article class="camp" style="left:15px"><div class="img" role="img" aria-label="Photo of children sewing with an instructor"></div><h4>Spring Camp</h4><p>Join us for a creative week during spring break! Children will learn sewing basics and create their own spring-themed projects.</p><div class="meta"><b>Age:</b><span>09 to 14</span><b>Total:</b><span style="text-align:right">200 Kids</span><b>Date:</b><span>21 Oct,2025</span><b>Duration:</b><span style="text-align:right">06 Days</span></div></article>
  <article class="camp" style="left:311px"><div class="img" role="img" aria-label="Photo of a girl at a sewing machine"></div><h4>Summer Camp</h4><p>Our popular summer program where kids design and create their own summer wardrobe items in a fun, supportive environment.</p><div class="meta"><b>Age:</b><span>09 to 14</span><b>Total:</b><span style="text-align:right">200 Kids</span><b>Date:</b><span>07 Jul,2025</span><b>Duration:</b><span style="text-align:right">06 Days</span></div></article>
  <article class="camp" style="left:607px"><div class="img" role="img" aria-label="Photo of a sewing class in a bright room"></div><h4>Autom Camp</h4><p>Get ready for cooler weather by creating cozy autumn accessories and clothing items in this creative camp Autumn Creative Camp.</p><div class="meta"><b>Age:</b><span>09 to 14</span><b>Total:</b><span style="text-align:right">200 Kids</span><b>Date:</b><span>21 Oct,2025</span><b>Duration:</b><span style="text-align:right">06 Days</span></div></article>
  <article class="camp" style="left:903px"><div class="img" role="img" aria-label="Photo of children at sewing machines with a teacher"></div><h4>Winter Camp</h4><p>Get ready for cooler weather by creating cozy autumn accessories and clothing items in this creative camp Autumn Creative Camp.</p><div class="meta"><b>Age:</b><span>09 to 14</span><b>Total:</b><span style="text-align:right">200 Kids</span><b>Date:</b><span>21 Oct,2025</span><b>Duration:</b><span style="text-align:right">06 Days</span></div></article>

  <div class="btn all-btn">View All Camps <span class="dot"><svg width="10" height="10" viewBox="0 0 10 10"><path d="M2 8L8 2M3 2h5v5" fill="none" stroke="#e8547a" stroke-width="1.6"/></svg></span></div>
</section>

<!-- CTA -->
<section>
  <svg class="cta-bg" width="1200" height="380" viewBox="0 0 1200 380"><path d="M0 30 C200 -10 380 40 600 20 C820 0 1000 -5 1200 20 L1200 340 C1000 380 820 330 600 350 C380 370 200 330 0 360Z" fill="#38ace0"/></svg>
  <h2 class="cta-title">READY FOR A CREATIVE ADVENTURE?</h2>
  <p class="cta-text">Spaces are limited to 8 children per camp to ensure personalized attention. Book now to secure your child's spot!</p>
  <div class="btn cta-btn">View All Camps <span class="dot"><svg width="10" height="10" viewBox="0 0 10 10"><path d="M2 8L8 2M3 2h5v5" fill="none" stroke="#fff" stroke-width="1.6"/></svg></span></div>
</section>

<!-- FAQ -->
<section>
  <div class="label" style="top:3528px">FREQUENTLY ASKED QUESTIONS</div>
  <h2 class="heading" style="top:3557px">Everything you need to know about <em>our camps</em></h2>

  <div class="faq open" style="top:3614px">Does my child need any prior knowledge?<p>We welcome children aged 9-14 years. This age range ensures that participants have the fine motor skills needed for sewing while still being excited about creative projects.</p><svg width="14" height="8" viewBox="0 0 14 8" style="top:28px"><path d="M1 7l6-6 6 6" fill="none" stroke="#1f2a37" stroke-width="1.6"/></svg></div>
  <div class="faq" style="top:3745px">How does the pick-up service work?<svg width="14" height="8" viewBox="0 0 14 8"><path d="M1 1l6 6 6-6" fill="none" stroke="#1f2a37" stroke-width="1.6"/></svg></div>
  <div class="faq" style="top:3826px">How many items of clothing are produced?<svg width="14" height="8" viewBox="0 0 14 8"><path d="M1 1l6 6 6-6" fill="none" stroke="#1f2a37" stroke-width="1.6"/></svg></div>
  <div class="faq" style="top:3907px">What should my child bring to camp?<svg width="14" height="8" viewBox="0 0 14 8"><path d="M1 1l6 6 6-6" fill="none" stroke="#1f2a37" stroke-width="1.6"/></svg></div>
  <div class="faq" style="top:3988px">What are the camp hours?<svg width="14" height="8" viewBox="0 0 14 8"><path d="M1 1l6 6 6-6" fill="none" stroke="#1f2a37" stroke-width="1.6"/></svg></div>
  <div class="faq" style="top:4069px">We offer pick-up from Zurich Main Station at times. Parents can arrange this during booking<svg width="14" height="8" viewBox="0 0 14 8"><path d="M1 1l6 6 6-6" fill="none" stroke="#1f2a37" stroke-width="1.6"/></svg></div>
  <div class="faq" style="top:4150px">What is your cancellation policy?<svg width="14" height="8" viewBox="0 0 14 8"><path d="M1 1l6 6 6-6" fill="none" stroke="#1f2a37" stroke-width="1.6"/></svg></div>
  <div class="faq" style="top:4231px">How many items of clothing are produced?<svg width="14" height="8" viewBox="0 0 14 8"><path d="M1 1l6 6 6-6" fill="none" stroke="#1f2a37" stroke-width="1.6"/></svg></div>
  <div class="faq" style="top:4312px">Each child completes their own unique clothing item during the week<svg width="14" height="8" viewBox="0 0 14 8"><path d="M1 1l6 6 6-6" fill="none" stroke="#1f2a37" stroke-width="1.6"/></svg></div>
  <div class="faq" style="top:4393px">What safety measures are in place?<svg width="14" height="8" viewBox="0 0 14 8"><path d="M1 1l6 6 6-6" fill="none" stroke="#1f2a37" stroke-width="1.6"/></svg></div>

  <div class="to-top"><svg width="16" height="16" viewBox="0 0 16 16" fill="none" stroke="#fff" stroke-width="2"><path d="M3 9l5-5 5 5M3 14l5-5 5 5"/></svg></div>
</section>

<!-- Footer -->
<footer>
  <svg class="footer-bg" width="1200" height="358" viewBox="0 0 1200 358"><path d="M0 20 C200 50 420 0 620 22 C820 44 1000 10 1200 26 L1200 358 L0 358Z" fill="#16243a"/></svg>
  <div class="footer-brand">Tovi-BrambleDays</div>
  <div class="follow">Follow Us: <i></i><i></i><i></i></div>

  <div class="f-head" style="left:364px">Quick Links</div>
  <div class="f-links">Home<br>About Us<br>Camps<br>How It Works<br>Contact</div>

  <div class="f-head" style="left:516px">Contact Us</div>
  <div class="f-contact" style="top:4676px"><i style="background:#2c3a52"><svg width="12" height="16" viewBox="0 0 12 16"><path d="M6 15s5-5 5-8.5a5 5 0 0 0-10 0C1 10 6 15 6 15z" fill="#fff"/></svg></i><span>A-123, There are many a<br>variations Zurich, Switzerland</span></div>
  <div class="f-contact" style="top:4744px"><i style="background:var(--blue)"><svg width="14" height="14" viewBox="0 0 14 14"><path d="M3 1l2 3-1.5 1.5a8 8 0 0 0 5 5L10 9l3 2-1 2.5C6 14 0 8 .5 2z" fill="#fff"/></svg></i><span>Phone: (044)-555 0187</span></div>
  <div class="f-contact" style="top:4796px"><i style="background:#2c3a52"><svg width="14" height="10" viewBox="0 0 14 10" fill="none" stroke="#fff" stroke-width="1.3"><rect x=".7" y=".7" width="12.6" height="8.6"/><path d="M1 1l6 5 6-5"/></svg></i><span>info@tovi-brambledays.ch</span></div>

  <div class="f-head" style="left:812px">Subscribe to newsletter</div>
  <div class="f-sub">latest updates, exclusive content, and special offers? Subscribe to our newsletter!</div>
  <div class="f-input">✉&nbsp; Your Email<i><svg width="12" height="12" viewBox="0 0 12 12" fill="none" stroke="#fff" stroke-width="1.8"><path d="M1 6h9M7 3l3 3-3 3"/></svg></i></div>

  <div class="f-rule"></div>
  <div class="copyright">© 2025 Tovi-BrambleDays. All Rights Reserved.</div>
</footer>

</body>
</html>
```